Web design for our new company

We need a web design for our product and for our company.
And the main is our Product tool called "veltor".
----------------------------------------------------------
[Our company's Goal]
Make organization’s communication smooth and healthy with transparency and efficiency for works and tasks in all levels with our workflow tool.

[Our Mission]
Our mission is to achieve business goals with customers.
We work together to identify the goals for your company, guides your strategy and bring the technology answers which best fit to achieve the goals.

[What we do]
We have a workflow tool "veltor"
- Very simple end-user configurable workflow for any company processes
(Targeting small-med size company)
- Graphical & fun features for startup users
- Simple and easy task control with outlook e-mail look & feel
- Non charged skill up guidance
- Additional features with;
Multiple delegation
Clear status for each owner
Task owner management console with due date reminders&reporting

Others
1. System Development & Implementation Service
Our client list includes a wide variety of small to medium to major sized enterprises.
We can offer from full-scratch based development to packaged system implementation.

2. Project Management(PM) Service
We will provide end-to-end PM service with experienced PM.
Our service is not only “managing” but “leading” to bring success to achieve the goal.

3.Consultation Service

Consulting services to a wide range of fields such as creating business strategy, business process Kaizen, IT system consultation and change management.

Target Market(s)

Business to Business
Mainly to medium size - startup company

Industry/Entity Type

It Company

Coding

Coded - Design and coding required

Number of Pages Required

5+ page

Colors
0255a3
33a6d7
86cfc6
33b8a4
add136
cadf82
fbf289
fee18a
faa54b

Requirements
Must have
• We need Pages for
• Company mission
• Service Overview
• Contact
• Privacy Policy
• Terms and Conditions
• =========================
• As there were some questions, I add followings.---------
• 1. File Format
• We are going to use Amazon web services to upload finished web files.
• The finished files should be ready to use by simply replacing images and text.
• Please provide me "easy to handle" template with "sophisticated design".
• Thanks!
• 2. Multiple Languages
• We need buttons for changing language.
• We will have this translated to German, English and Japanese.
• Thank you so much!!
Nice to have
• These are current Logos and will be a next project to revise them...
• Attached Company Profile and Logo design
• 1. Company Profile
• 2. Our Company Logo
• 3. Our Product Logo -> This is most close to our image of design base.
• 4. Product Logo for PPT Header
• All just for your reference.
• ---------
• As there were some request, I added attachment as for contents for Our mission page.
Should not have
• I hope to see some unique designs.
• (Sorry please ignore my last update as I checked with our CEO.
• Bootstrap is absolutely good template.)

```html
<!DOCTYPE html>
<html lang="en">
<head>
<meta charset="utf-8">
<title>veltor — Our Mission</title>
<link href="https://fonts.googleapis.com/css2?family=Arimo:wght@400;700&display=swap" rel="stylesheet">
<style>
  :root {
    --navy: #062a66;
    --navy-text: #0e2a5e;
    --brand-blue: #0255a3;
    --nav-blue: #0c63b5;
    --lime: #add136;
    --ink: #1a1a1a;
    --grey-band: #f2f2f2;
    --white: #ffffff;
    --sky-top: #7fa9d6;
    --sky-mid: #c9d8ea;
    --sun: #f4dcb0;
    --shade: #3b4f6e;
  }
  * { margin: 0; padding: 0; box-sizing: border-box; }
  html, body { width: 1200px; height: 2812px; overflow: hidden; }
  body {
    position: relative;
    background: var(--white);
    font-family: "Arimo", Arial, sans-serif;
    color: var(--ink);
  }
  .abs { position: absolute; }

  /* header */
  .top-rule { left: 0; top: 0; width: 1200px; height: 10px; background: var(--navy); }
  .site-header { left: 0; top: 10px; width: 1200px; height: 72px; background: var(--white); }
  .brand { left: 14px; top: 14px; display: flex; align-items: center; gap: 8px; }
  .brand-name { font-size: 38px; font-weight: 700; color: var(--brand-blue); line-height: 1; }
  .brand-mark { width: 30px; height: 30px; background: var(--brand-blue); }
  .main-nav { left: 272px; top: 30px; display: flex; font-size: 23px; font-weight: 700; color: var(--nav-blue); }
  .main-nav a { color: inherit; text-decoration: none; position: absolute; white-space: nowrap; top: 0; }
  .main-nav .is-active { color: var(--lime); }

  /* hero */
  .hero {
    left: 0; top: 82px; width: 1200px; height: 559px;
    background:
      radial-gradient(ellipse 260px 200px at 640px 330px, rgba(255,240,210,0.95), rgba(255,240,210,0) 70%),
      linear-gradient(180deg, var(--sky-top) 0%, var(--sky-mid) 45%, var(--sun) 60%, #9fb3c9 75%, var(--shade) 100%);
  }
  .hero-band { left: 0; top: 154px; width: 1200px; height: 244px; background: rgba(255,255,255,0.55); }
  .hero-title { left: 103px; top: 190px; font-size: 62px; font-weight: 700; color: var(--navy-text); letter-spacing: -1px; }
  .hero-copy { left: 103px; top: 264px; font-size: 22px; font-weight: 700; color: var(--navy-text); line-height: 34px; }
  .slider-dots { left: 568px; top: 608px; display: flex; gap: 7px; }
  .slider-dots span { width: 14px; height: 14px; border-radius: 50%; background: var(--white); }

  /* content sections */
  .section-title { left: 0; width: 1200px; text-align: center; font-size: 28px; color: var(--ink); text-transform: uppercase; }
  .section-text { left: 60px; width: 1080px; text-align: center; font-size: 24px; line-height: 29px; }
  .legal-text { left: 70px; width: 1090px; text-align: center; font-size: 23px; line-height: 28px; }

  .service-card { top: 1082px; width: 300px; }
  .service-card .thumb { width: 300px; height: 143px; background: linear-gradient(180deg, var(--sky-top), var(--sun) 55%, var(--shade)); }
  .service-card p { font-size: 18px; line-height: 26px; height: 109px; overflow: hidden; padding: 12px 0 0 2px; }
  .service-card .cta {
    display: block; width: 300px; height: 55px; background: var(--navy); color: var(--white);
    font-size: 28px; text-align: center; line-height: 55px; text-decoration: none;
  }

  .privacy-band { left: 0; top: 1431px; width: 1200px; height: 590px; background: var(--grey-band); }
  .privacy-photo {
    left: 319px; top: 1691px; width: 587px; height: 280px;
    background:
      radial-gradient(ellipse 120px 90px at 300px 120px, rgba(255,240,210,0.9), rgba(255,240,210,0) 70%),
      linear-gradient(180deg, var(--sky-top), var(--sky-mid) 40%, var(--sun) 58%, var(--shade));
  }

  /* contact */
  .contact {
    left: 0; top: 2302px; width: 1200px; height: 398px;
    background:
      radial-gradient(ellipse 260px 160px at 700px 220px, rgba(255,245,225,0.95), rgba(255,245,225,0) 70%),
      linear-gradient(180deg, #aac6e4 0%, #dbe6f1 45%, #f1e2c7 62%, #a7b8cc 82%, #6f84a2 100%);
  }
  .contact-title { top: 2330px; color: var(--navy-text); }
  .contact-item { top: 2446px; font-size: 42px; line-height: 51px; color: #14408a; }

  /* footer */
  .site-footer { left: 0; top: 2700px; width: 1200px; height: 112px; background: var(--navy); color: var(--white); }
  .copyright { left: 261px; top: 2728px; font-size: 24px; color: var(--white); }
  .social-dot { left: 628px; top: 2728px; width: 36px; height: 36px; border-radius: 50%; background: var(--white); }
  .social-link { left: 672px; top: 2726px; font-size: 24px; color: var(--white); }
  .lang-switch { left: 1114px; top: 2721px; width: 42px; height: 42px; }
</style>
</head>
<body>

  <div class="abs top-rule"></div>
  <header class="abs site-header">
    <div class="abs brand"><span class="brand-name">veltor</span><span class="brand-mark"></span></div>
    <nav class="abs main-nav">
      <a class="is-active" style="left:0">MISSION</a>
      <a style="left:133px">OVERVIEW</a>
      <a style="left:275px">PRIVACY POLICY</a>
      <a style="left:470px">TERMS AND CONDITIONS</a>
      <a style="left:774px">CONTACTS</a>
    </nav>
  </header>

  <section class="abs hero" role="img" aria-label="Photo of two business people shaking hands by a sunlit office window, with a tablet showing charts on a desk"></section>
  <div class="abs hero-band"></div>
  <h1 class="abs hero-title">[OUR MISSION]</h1>
  <p class="abs hero-copy">Our mission is to achieve business goals with customers.<br>We work together to identify the goals for your company, guides<br>your strategy and bring the technology answers which best fit to achieve the goals.</p>
  <div class="abs slider-dots"><span></span><span></span><span></span><span></span></div>

  <h2 class="abs section-title" style="top:690px">Our Company’s Goal</h2>
  <p class="abs section-text" style="top:752px">Make organization’s communication smooth and healthy with transparency and efficiency for<br>works and tasks in all levels with our workflow tool.</p>

  <h2 class="abs section-title" style="top:840px">Our Mission</h2>
  <p class="abs section-text" style="top:897px">Our mission is to achieve business goals with customers.<br>We work together to identify the goals for your company, guides your strategy and bring the technology<br>answers which best fit to achieve the goals.</p>

  <h2 class="abs section-title" style="top:1020px">What We Do</h2>

  <article class="abs service-card" style="left:99px">
    <div class="thumb" role="img" aria-label="Photo of a business handshake in a bright office"></div>
    <p>Lorem ipsum dolor sit amet, con sectetur adipiscing elit. Etiam elit libero, commodo et eleifend quis, congue quis lectus. Duis dapibus molestie tempor. Phasellus</p>
    <a class="cta">CLICK ME</a>
  </article>
  <article class="abs service-card" style="left:433px">
    <div class="thumb" role="img" aria-label="Photo of a business handshake in a bright office"></div>
    <p>Lorem ipsum dolor sit amet, con sectetur adipiscing elit. Etiam elit libero, commodo et eleifend quis, congue quis lectus. Duis dapibus molestie tempor. Phasellus</p>
    <a class="cta">CLICK ME</a>
  </article>
  <article class="abs service-card" style="left:767px">
    <div class="thumb" role="img" aria-label="Photo of a business handshake in a bright office"></div>
    <p>Lorem ipsum dolor sit amet, con sectetur adipiscing elit. Etiam elit libero, commodo et eleifend quis, congue quis lectus. Duis dapibus molestie tempor. Phasellus</p>
    <a class="cta">CLICK ME</a>
  </article>

  <section class="abs privacy-band"></section>
  <h2 class="abs section-title" style="top:1436px">Privacy Policy</h2>
  <p class="abs legal-text" style="top:1492px">Lorem ipsum dolor sit amet, consectetur adipiscing elit. Etiam elit libero, commodo et eleifend quis, congue quis lectus. Duis dapibus molestie tempor. Phasellus urna enim, tempus ac tincidunt vestibulum, posuere et dui. Maecenas dapibus, lorem vitae porta congue, eros orci accumsan eros, eget pulvinar elit ex quis turpis. Nullam molestie, orci id molestie condimentum, mi tortor sollicitudin nisi, finibus malesuada enim sapien nec felis. Mauris vitae consequat odio. Donec sollicitudin pretium sodales. Curabitur suscipit sem mauris, non tincidunt lectus blandit et.</p>
  <div class="abs privacy-photo" role="img" aria-label="Photo of two business people shaking hands by an office window at sunset"></div>

  <h2 class="abs section-title" style="top:2047px">Terms and Conditions</h2>
  <p class="abs legal-text" style="top:2103px">Lorem ipsum dolor sit amet, consectetur adipiscing elit. Etiam elit libero, commodo et eleifend quis, congue quis lectus. Duis dapibus molestie tempor. Phasellus urna enim, tempus ac tincidunt vestibulum, posuere et dui. Maecenas dapibus, lorem vitae porta congue, eros orci accumsan eros, eget pulvinar elit ex quis turpis. Nullam molestie, orci id molestie condimentum, mi tortor sollicitudin nisi, finibus malesuada enim sapien nec felis. Mauris vitae consequat odio. Donec sollicitudin pretium sodales. Curabitur suscipit sem mauris, non tincidunt lectus blandit et.</p>

  <section class="abs contact" role="img" aria-label="Faded photo of a business handshake in a sunlit office with a statistics tablet"></section>
  <h2 class="abs section-title contact-title">Contact Us</h2>
  <div class="abs contact-item" style="left:75px">TEL<br>+63 555-0142</div>
  <div class="abs contact-item" style="left:382px">EMAIL<br>veltor@mailhub.com</div>
  <div class="abs contact-item" style="left:806px">ADDRESS<br>#123 lorem ipsum<br>dolor sit amet,</div>

  <footer class="abs site-footer"></footer>
  <div class="abs copyright">ALL RIGHTS RESERVED 2018</div>
  <div class="abs social-dot"></div>
  <div class="abs social-link">www.linkpage.com/veltor</div>
  <svg class="abs lang-switch" viewBox="0 0 42 42" aria-label="Change language" fill="none" stroke="#ffffff" stroke-width="2">
    <circle cx="21" cy="21" r="18"/>
    <ellipse cx="21" cy="21" rx="8" ry="18"/>
    <line x1="3" y1="21" x2="39" y2="21"/>
    <path d="M6 12 H36 M6 30 H36"/>
  </svg>

</body>
</html>
```